Corvell Ashdown Website

Updated website for Corvell Ashdown Dry Cleaners & Garment Care.

Please look at www.tindalepressers.example we really like this site!!!

We are not set on colors or fonts. Looking for an professional easy to use site that looks and works even better on a mobile device. 90% of our customers visit us on cell phones.

Target Market(s)

We are located in an up scale area with young trendy individuals but, also very successful mature customers as well. Probably geared more to tech savvy younger crowd.

Industry/Entity Type

Dry Cleaning

Coding

Coded - Design and coding required

Font styles to use
Serif
Script

Colors
85abd2
85cae6
cee9f5
cfdeed
757575

Requirements
Must have
• Must look good on a mobile device and have sign up for our pick up and delivery. Geographical pick up and delivery perimeters would be great as well. Capturing emails and other user data for future marketing. We do a lot of advertising.
• Please look at www.tindalepressers.example we really like this site!!!
• Search engine optimized.
• Also we are adding a new POS system that will have a login for customers and possibly an app.
Nice to have
• 100% satisfaction guaranteed and scrolling reviews somewhere on the page.

```html
<!DOCTYPE html>
<html lang="en">
<head>
<meta charset="utf-8">
<title>Corvell Ashdown Dry Cleaners &amp; Garment Care</title>
<link rel="stylesheet" href="https://fonts.googleapis.com/css2?family=Montserrat:wght@400;500;600;700&family=Open+Sans:wght@400;600&display=swap">
<style>
:root{
  --blue:#5f8fc9;
  --blue-soft:#85abd2;
  --sky:#85cae6;
  --sky-pale:#cee9f5;
  --band:#7399cb;
  --text:#5a5a5a;
  --grey:#757575;
  --light:#f2f2f2;
  --footer:#2d2d2d;
  --white:#fff;
}
*{box-sizing:border-box;margin:0;padding:0}
html,body{width:1200px;height:3416px;overflow:hidden}
body{position:relative;font-family:"Open Sans",Arial,sans-serif;color:var(--text);background:var(--white);font-size:13px}
.abs{position:absolute}
.heading{font-family:"Montserrat",sans-serif;color:var(--blue);font-weight:600;text-align:center;letter-spacing:1px}
.sub{text-align:center;font-size:12.5px;color:var(--text)}

.site-header{top:0;left:0;width:1200px;height:96px;border-top:4px solid var(--blue-soft);background:var(--white);box-shadow:0 1px 4px rgba(0,0,0,.08)}
.brand{left:87px;top:26px;display:flex;align-items:center;gap:10px;font-family:"Montserrat",sans-serif;font-size:22px;font-weight:500;color:#3c4a5a}
.brand-dot{width:16px;height:16px;border-radius:50%;background:var(--blue-soft)}
.nav{right:86px;top:40px;display:flex;gap:46px;font-family:"Montserrat",sans-serif;font-size:12.5px;font-weight:500;color:#444;letter-spacing:.3px}
.nav .active{color:var(--blue)}

.hero{top:96px;left:0;width:1200px;height:546px;background:linear-gradient(90deg,#f4f4f4 0,#ececec 40%,#dcdde0 100%)}
.hero-photo{left:467px;top:0;width:733px;height:546px;background:linear-gradient(120deg,#e7e3df 0,#c8d3e6 45%,#5c7fc0 62%,#d9dadd 100%)}
.hero-title{left:86px;top:170px;font-family:"Montserrat",sans-serif;color:var(--blue-soft);font-size:31px;font-weight:500;line-height:44px;letter-spacing:.5px}
.hero-input{left:87px;top:268px;width:389px;height:46px;background:var(--white);border:1px solid #ccc;font-size:12px;padding:14px 14px;color:#666}
.btn{background:var(--blue-soft);color:var(--white);font-family:"Montserrat",sans-serif;font-weight:600;font-size:14px;text-align:center;letter-spacing:.5px}
.hero-btn{left:87px;top:336px;width:139px;height:44px;line-height:44px}

.services-title{top:684px;left:0;width:1200px;font-size:29px}
.services-sub{top:736px;left:0;width:1200px}
.card{top:800px;width:246px}
.card-img{height:183px}
.card-title{margin-top:22px;font-family:"Montserrat",sans-serif;font-size:16px;color:var(--blue-soft);text-align:center;font-weight:500;letter-spacing:.5px}
.card-text{margin-top:12px;font-size:11.5px;line-height:25px;text-align:center;color:var(--text)}
.arrow{width:20px;height:80px}

.welcome{top:1161px;left:0;width:1200px;height:428px}
.welcome-panel{left:0;top:0;width:674px;height:428px;background:var(--sky)}
.welcome-photo{left:674px;top:0;width:526px;height:428px;background:linear-gradient(180deg,#9fc0dc 0,#c9d8e6 30%,#5b4d4b 50%,#7f8a6c 75%,#9aa18c 100%)}
.welcome-kicker{left:121px;top:58px;color:var(--white);font-family:"Montserrat",sans-serif;font-size:24px;letter-spacing:1px}
.welcome-name{left:121px;top:96px;color:var(--white);font-family:"Montserrat",sans-serif;font-size:36px;font-weight:600;letter-spacing:1.5px}
.welcome-text{left:121px;top:168px;width:500px;color:var(--white);font-size:11.5px;line-height:29px}
.welcome-btn{left:121px;top:308px;width:214px;height:52px;border:2px solid var(--white);border-radius:26px;color:var(--white);font-family:"Montserrat",sans-serif;font-size:11.5px;font-weight:600;text-align:center;line-height:48px}

.coverage-title{top:1633px;left:0;width:1200px;font-size:29px}
.coverage-sub{top:1688px;left:0;width:1200px}
.select{left:264px;top:1737px;width:670px;height:41px;border:1px solid #bbb;font-size:12px;padding:11px 14px;color:#555}
.map{left:139px;top:1810px;width:922px;height:451px;background:linear-gradient(90deg,#ecebe6 0,#efeee9 50%,#e5eedd 80%,#b9d9a5 100%);border:1px solid #ddd;overflow:hidden}
.map svg{position:absolute;left:0;top:0}

.guarantee{top:2309px;left:0;width:1200px;height:266px;background:var(--band)}
.badge{left:196px;top:34px;width:200px;height:200px;border-radius:50%;border:6px solid var(--white)}
.guarantee-title{left:437px;top:80px;color:var(--white);font-family:"Montserrat",sans-serif;font-size:22px;font-weight:500;letter-spacing:.5px}
.guarantee-text{left:442px;top:134px;width:600px;color:var(--white);font-size:11.5px;line-height:25px}

.reviews{top:2575px;left:0;width:1200px;height:481px;background:var(--light)}
.reviews-title{top:30px;left:0;width:1200px;font-size:29px}
.reviews-sub{top:83px;left:0;width:1200px}
.review{top:157px;width:327px}
.review-card{height:194px;background:var(--white);padding:22px 26px;box-shadow:0 1px 3px rgba(0,0,0,.05)}
.review-top{display:flex;align-items:center;gap:10px}
.quote{font-family:Georgia,serif;font-size:30px;color:#999;line-height:20px;font-weight:700}
.stars{color:#f2a81d;font-size:13px;letter-spacing:1px}
.review-text{margin-top:12px;font-size:11.5px;line-height:25px;color:#666}
.review-name{margin-top:38px;margin-left:6px;font-family:"Montserrat",sans-serif;font-size:13.5px;font-weight:600;color:#333}
.review-date{margin-left:6px;font-size:11px;color:#666;margin-top:4px}

.footer{top:3056px;left:0;width:1200px;height:360px;background:var(--footer);color:var(--white)}
.foot-h{font-family:"Montserrat",sans-serif;font-size:16px;font-weight:500;letter-spacing:.5px}
.field{background:var(--white);color:#666;font-size:11px;padding:10px 14px}
.send{left:87px;top:232px;width:118px;height:36px;line-height:36px;background:var(--sky)}
.address{left:612px;top:78px;font-size:14px;line-height:18px}
.address p{margin-bottom:18px}
.links{left:911px;top:78px;font-size:14px;line-height:34px;list-style:none}
.rule{left:87px;top:291px;width:1026px;height:1px;background:#555}
.copyright{left:87px;top:320px;font-size:11px}
.social{left:904px;top:308px;display:flex;gap:6px}
.social span{width:37px;height:37px;border-radius:50%;border:1.5px solid var(--white)}
</style>
</head>
<body>

<header class="site-header abs">
  <div class="brand abs"><span class="brand-dot"></span>Corvell Ashdown</div>
  <nav class="nav abs">
    <span class="active">HOME</span><span>ABOUT US</span><span>PICK UP &amp; DELIVERY</span><span>SERVICES</span><span>CONTACT US</span>
  </nav>
</header>

<section class="hero abs">
  <div class="hero-photo abs" role="img" aria-label="Staff member steaming a blue checked shirt on a hanger"></div>
  <h1 class="hero-title abs">SIGN UP FOR<br>OUR PICK UP &amp; DELIVERY</h1>
  <div class="hero-input abs">Enter your keyword :</div>
  <div class="hero-btn btn abs">SIGN UP</div>
</section>

<h2 class="services-title heading abs">OUR SERVICES</h2>
<p class="services-sub sub abs">Our passion started well over 50 years ago with our original store 'Brightpress' which was located in the heart of Downtown</p>

<svg class="arrow abs" style="left:38px;top:928px" viewBox="0 0 20 80"><path d="M16 2 L4 40 L16 78" fill="none" stroke="#999" stroke-width="1.5"/></svg>
<svg class="arrow abs" style="left:1142px;top:928px" viewBox="0 0 20 80"><path d="M4 2 L16 40 L4 78" fill="none" stroke="#999" stroke-width="1.5"/></svg>

<article class="card abs" style="left:87px">
  <div class="card-img" role="img" aria-label="Dark suit with striped tie and pocket square" style="background:linear-gradient(135deg,#3a3d44,#16181c)"></div>
  <h3 class="card-title">DRY CLEANING</h3>
  <p class="card-text">At Corvell Ashdown we specialize in dry cleaning of high-end clothing and fine linens. Our plant is specifically designed</p>
</article>
<article class="card abs" style="left:346px">
  <div class="card-img" role="img" aria-label="Folded shirts in green and purple" style="background:linear-gradient(135deg,#9aa22a,#4b2d63)"></div>
  <h3 class="card-title">SHIRT LAUNDERING</h3>
  <p class="card-text">Bringing your shirts to Corvell Ashdown Drycleaners will help you look your profes-sional best each and every day.</p>
</article>
<article class="card abs" style="left:606px">
  <div class="card-img" role="img" aria-label="Brown leather jacket" style="background:linear-gradient(135deg,#5a3e2c,#2a1d15)"></div>
  <h3 class="card-title">SUEDE &amp; LEATHER</h3>
  <p class="card-text">Suede and Leather need a special kind of cleaning. Cleaning these precious items is a wrong with improper cleaning.</p>
</article>
<article class="card abs" style="left:865px">
  <div class="card-img" role="img" aria-label="Stack of folded turquoise towels" style="background:linear-gradient(135deg,#6fd0c6,#bfc7c9)"></div>
  <h3 class="card-title">WASH &amp; FOLD</h3>
  <p class="card-text">Life can be hectic. Let us help you with your laundry! Give us your dirty laundry and we it and package it up for you.</p>
</article>

<section class="welcome abs">
  <div class="welcome-panel abs"></div>
  <div class="welcome-photo abs" role="img" aria-label="Storefront of the dry cleaning shop with signage and flowers"></div>
  <p class="welcome-kicker abs">WELCOME TO</p>
  <h2 class="welcome-name abs">CORVELL ASHDOWN</h2>
  <p class="welcome-text abs">Our passion started well over 50 years ago with our original store 'Brightpress' which was located in the heart of Downtown Halverton, where Bock-E stands today. We have now been in Larkmere for over 38 years! We are a family owned and operated business that provides quality and exceptional service. We take pride in our work and it shows!</p>
  <div class="welcome-btn abs">CLICK HERE FOR MORE INFO</div>
</section>

<h2 class="coverage-title heading abs">COVERAGE AREA</h2>
<p class="coverage-sub sub abs">We currently service Larkmere and all surrounding cities please keep in mind we can provide the service</p>
<div class="select abs">Location
  <svg class="abs" style="right:14px;top:16px" width="9" height="6" viewBox="0 0 9 6"><path d="M0 0h9L4.5 6z" fill="#444"/></svg>
</div>
<div class="map abs" role="img" aria-label="Street map of the town centre showing the pick-up and delivery perimeter around the shop">
  <svg width="922" height="451" viewBox="0 0 922 451" aria-hidden="true">
    <circle cx="461" cy="225" r="190" fill="rgba(133,171,210,.18)" stroke="#5f8fc9" stroke-width="2" stroke-dasharray="10 7"/>
    <circle cx="461" cy="225" r="110" fill="rgba(133,202,230,.22)" stroke="#85cae6" stroke-width="1.5" stroke-dasharray="6 5"/>
    <path d="M461 190c-13 0-23 10-23 23 0 17 23 40 23 40s23-23 23-40c0-13-10-23-23-23z" fill="#5f8fc9"/>
    <circle cx="461" cy="213" r="8" fill="#fff"/>
  </svg>
</div>

<section class="guarantee abs">
  <div class="badge abs" role="img" aria-label="Satisfaction guaranteed seal"></div>
  <h2 class="guarantee-title abs">SATISFACTION GUARANTEED</h2>
  <p class="guarantee-text abs">Sed ut perspiciatis unde omnis iste natus error sit voluptatem accusantium doloremque laudantium, totam rem illo inventore veritatis et quasi architecto beatae vitae dicta sunt explicabo.</p>
</section>

<section class="reviews abs">
  <h2 class="reviews-title heading abs">CUSTOMER REVIEWS</h2>
  <p class="reviews-sub sub abs">We currently service Larkmere and all surrounding cities please keep in mind we can provide the service</p>
  <svg class="arrow abs" style="left:38px;top:210px" viewBox="0 0 20 80"><path d="M16 2 L4 40 L16 78" fill="none" stroke="#999" stroke-width="1.5"/></svg>
  <svg class="arrow abs" style="left:1142px;top:210px" viewBox="0 0 20 80"><path d="M4 2 L16 40 L4 78" fill="none" stroke="#999" stroke-width="1.5"/></svg>
  <div class="review abs" style="left:87px">
    <div class="review-card"><div class="review-top"><span class="quote">&ldquo;</span><span class="stars">★★★★★</span></div>
    <p class="review-text">Sed ut perspiciatis unde omnis iste natus error sit voluptatem accusantium doloremque laudantium, totam rem aperiam, eaque ipsa quae ab illo inven-tore veritatis et quasi architecto beatae vitae dicta sunt explicabo.</p></div>
    <p class="review-name">Dana Ellery</p><p class="review-date">Posted on 28-July 2018</p>
  </div>
  <div class="review abs" style="left:437px">
    <div class="review-card"><div class="review-top"><span class="quote">&ldquo;</span><span class="stars">★★★★★</span></div>
    <p class="review-text">Sed ut perspiciatis unde omnis iste natus error sit voluptatem accusantium doloremque laudantium, totam rem aperiam, eaque ipsa quae ab illo inven-tore veritatis et quasi architecto beatae vitae dicta sunt explicabo.</p></div>
    <p class="review-name">Dana Ellery</p><p class="review-date">Posted on 28-July 2018</p>
  </div>
  <div class="review abs" style="left:788px">
    <div class="review-card"><div class="review-top"><span class="quote">&ldquo;</span><span class="stars">★★★★★</span></div>
    <p class="review-text">Sed ut perspiciatis unde omnis iste natus error sit voluptatem accusantium doloremque laudantium, totam rem aperiam, eaque ipsa quae ab illo inven-tore veritatis et quasi architecto beatae vitae dicta sunt explicabo.</p></div>
    <p class="review-name">Dana Ellery</p><p class="review-date">Posted on 28-July 2018</p>
  </div>
</section>

<footer class="footer abs">
  <h3 class="foot-h abs" style="left:87px;top:40px">CONTACT US</h3>
  <div class="field abs" style="left:87px;top:86px;width:209px;height:37px">Name :</div>
  <div class="field abs" style="left:310px;top:86px;width:209px;height:37px">Email :</div>
  <div class="field abs" style="left:87px;top:130px;width:209px;height:36px">Phone :</div>
  <div class="field abs" style="left:310px;top:130px;width:209px;height:36px">Company :</div>
  <div class="field abs" style="left:87px;top:175px;width:432px;height:46px">Message :</div>
  <div class="send btn abs">SEND</div>

  <h3 class="foot-h abs" style="left:610px;top:40px">ADDRESS</h3>
  <div class="address abs">
    <p>ADDRESS<br>2210 E. Larkmere Blvd.<br>Larkmere, MN 55000</p>
    <p>PHONE<br>555-014-2290</p>
    <p>EMAIL<br>info@corvellashdown.example</p>
  </div>

  <h3 class="foot-h abs" style="left:911px;top:40px">LINKS</h3>
  <ul class="links abs"><li>Home</li><li>About Us</li><li>Pick Up &amp; Delivery</li><li>Services</li><li>Contact Us</li></ul>

  <div class="rule abs"></div>
  <p class="copyright abs">© Copyright 2018 Corvell Ashdown.All Rights Reserved</p>
  <div class="social abs"><span></span><span></span><span></span><span></span><span></span></div>
</footer>

</body>
</html>
```